Flyer Design Project - Bra Shop

Hi all,

I want to have a flyer with theme colour Pink or Red.
I will upload one of my previous flyers.

requirement:
*I need to keep the contact detail, address and map.(you can edit it as different style if you want.)

*I need to keep our store logo and store name:
Velmotine
Lingerie

*The information in flyer:

We sell
Push / non push up bras
Maternity
Silqe
Bottoms
Pajamas
Shape wears
Sexy lingerie
Stockings, suspenders
Garters
Crystal phonecase
And much more

*At the top right coner of flyer, please write down '$10 Voucher' because I want it to be a Voucher.

*At the bottom of the flyer, please write (small font size ):
"**Only one flyer voucher can be used in one purchase when price is above $50 and below $100. Two flyer vouchers can be used in one purchase when price is not less than $100.

aged 30+ to 70; they are relatively wealthy.

Store

• the footnote changed:

**Only one flyer voucher can be used in one purchase when price is above $50 and below $100. Two flyer vouchers can be used in one purchase when price is not less than $100.
• I don't want a lady or people on flyer.
thanks

```html
<!DOCTYPE html>
<html lang="en">
<head>
<meta charset="utf-8">
<title>Velmotine Lingerie Flyer</title>
<link href="https://fonts.googleapis.com/css2?family=Great+Vibes&family=Arimo:wght@400;700&display=swap" rel="stylesheet">
<style>
  :root {
    --stage: #eeeeee;
    --pink-deep: #d3145f;
    --pink-mid: #e2367f;
    --pink-soft: #f06aa5;
    --white: #ffffff;
    --shadow: rgba(90, 0, 35, 0.45);
  }
  * { margin: 0; padding: 0; box-sizing: border-box; }
  html, body { width: 1200px; height: 900px; overflow: hidden; }
  body {
    background: linear-gradient(180deg, #f7f7f7 0%, var(--stage) 100%);
    font-family: "Arimo", Arial, sans-serif;
    position: relative;
  }
  .flyer {
    position: absolute;
    left: 318px; top: 48px;
    width: 565px; height: 802px;
    background: linear-gradient(160deg, var(--pink-mid) 0%, var(--pink-deep) 55%, #d92a6e 100%);
    overflow: hidden;
    color: var(--white);
    box-shadow: 0 0 3px rgba(0,0,0,0.15);
  }
  .flyer-curves { position: absolute; inset: 0; width: 100%; height: 100%; }
  .voucher {
    position: absolute;
    left: 377px; top: 34px;
    width: 200px; height: 102px;
    background: var(--pink-deep);
    border-radius: 14px 0 0 14px;
    display: flex; flex-direction: column; align-items: center; justify-content: center;
    font-weight: 700;
    line-height: 1;
    box-shadow: 0 1px 3px var(--shadow);
  }
  .voucher::after {
    content: "";
    position: absolute;
    inset: 5px -10px 5px 5px;
    border: 1px dashed rgba(255,255,255,0.8);
    border-radius: 10px 0 0 10px;
  }
  .voucher-amount { font-size: 44px; padding-right: 20px; }
  .voucher-label { font-size: 29px; margin-top: 4px; padding-right: 20px; }
  .brand-name {
    position: absolute;
    left: 48px; top: 72px;
    font-family: "Great Vibes", cursive;
    font-size: 64px;
    line-height: 1;
  }
  .brand-tagline {
    position: absolute;
    left: 74px; top: 152px;
    font-size: 20px;
    letter-spacing: 19px;
  }
  .product-photo {
    position: absolute;
    left: 45px; top: 218px;
    width: 472px; height: 363px;
    border-radius: 40%;
    background: radial-gradient(ellipse at 50% 50%, rgba(235, 70, 120, 0.85) 0%, rgba(225, 60, 110, 0.5) 45%, rgba(220, 40, 100, 0) 72%);
  }
  .headline {
    position: absolute;
    left: 96px; top: 178px;
    font-family: "Great Vibes", cursive;
    font-size: 116px;
    line-height: 1;
    text-shadow: 2px 2px 3px var(--shadow);
  }
  .product {
    position: absolute;
    line-height: 1;
    transform: translateY(-50%);
    white-space: nowrap;
    text-shadow: 1px 1px 2px var(--shadow);
  }
  .product--sm { font-size: 26px; }
  .product--md { font-size: 34px; }
  .product--lg { font-size: 39px; }
  .product--xl { font-size: 44px; }
  .closing {
    position: absolute;
    left: 80px; top: 545px;
    font-family: "Great Vibes", cursive;
    font-size: 60px;
    line-height: 1;
    text-shadow: 2px 2px 3px var(--shadow);
  }
  .store-info { position: absolute; left: 29px; top: 612px; }
  .hours-title { font-size: 14px; font-weight: 700; }
  .hours-line { font-size: 14px; margin-top: 4px; }
  .contact { margin-top: 14px; font-size: 18px; line-height: 23px; }
  .contact strong { font-weight: 700; }
  .footnote {
    position: absolute;
    left: 29px; top: 758px;
    width: 260px;
    font-size: 8.5px;
    line-height: 10.5px;
  }
  .store-map {
    position: absolute;
    left: 323px; top: 611px;
    width: 218px; height: 178px;
    background: linear-gradient(150deg, rgba(255,255,255,0.12) 0%, rgba(255,255,255,0.05) 100%);
    border-radius: 4px;
  }
</style>
</head>
<body>
  <main class="flyer">
    <svg class="flyer-curves" viewBox="0 0 565 802" aria-hidden="true">
      <path d="M0 0 H220 C150 120 110 260 150 420 C180 560 120 700 0 802 Z" fill="#ffffff" opacity="0.07"/>
      <path d="M330 0 H565 V300 C500 220 430 120 330 0 Z" fill="#ffffff" opacity="0.08"/>
      <path d="M420 0 C470 160 520 300 565 380 V0 Z" fill="#ffffff" opacity="0.06"/>
      <path d="M0 560 C160 600 320 640 565 600 V802 H0 Z" fill="#b80c50" opacity="0.15"/>
    </svg>

    <div class="voucher">
      <span class="voucher-amount">$10</span>
      <span class="voucher-label">Voucher</span>
    </div>

    <div class="brand-name">Velmotine</div>
    <div class="brand-tagline">Lingerie</div>

    <div class="product-photo" role="img" aria-label="Photo of a pink lace bra and matching briefs"></div>

    <h1 class="headline">We Sell</h1>

    <span class="product product--sm" style="left:133px; top:321px;">Push / non push up bras</span>
    <span class="product product--md" style="left:77px; top:357px;">Crystal phonecase</span>
    <span class="product product--sm" style="left:376px; top:347px;">Maternity</span>
    <span class="product product--md" style="left:143px; top:400px;">Bottoms</span>
    <span class="product product--lg" style="left:306px; top:394px;">Garters</span>
    <span class="product product--md" style="left:76px; top:440px;">Shape wears</span>
    <span class="product product--sm" style="left:299px; top:433px;">Pajamas</span>
    <span class="product product--md" style="left:113px; top:482px;">Sexy lingerie</span>
    <span class="product product--xl" style="left:320px; top:477px;">Silqe</span>
    <span class="product product--sm" style="left:146px; top:518px;">Stockings, suspenders</span>

    <div class="closing">And much more</div>

    <section class="store-info">
      <p class="hours-title">Open hour:</p>
      <p class="hours-line">Mon - Sat 10:00am - 5:30pm</p>
      <p class="hours-line">Sun 10:00am - 5:00pm</p>
      <p class="contact">
        <strong>Address:</strong> Shop 3/218<br>
        Harbour Crest Rd, NSW 2041<br>
        <strong>Phone:</strong> 02 9000 4817
      </p>
    </section>

    <p class="footnote">*Only one flyer voucher can be used in one purchase when price is above $50 and below $100. Two flyer vouchers can be used in one purchase when price is not less than $100.</p>

    <div class="store-map" role="img" aria-label="Street map showing the shop location near the main road"></div>
  </main>
</body>
</html>
```